Bussines Card Maple
MAPLE BARBER SHOP
Project: Bussines Card Maple
Bussines Card Maple - Salon & Spa
Creative Brief
Bright & Fun-filled
418 ELM RD SUITE 1 SPARKILL, N.Y. 10976
maplebarbershop@examplemail.com
Concepts
Business Card Design Hair Salon
Stationery Package for Nail Salon
lunarbakehouse lunarbakehouse
Phone number, fax, and info just make it bigger please.
Please only use Maple Barber Shop but use the same colors you've been using. Just discard the logo on the front side but on the back use the logo only. Thank you

```html
<!DOCTYPE html>
<html lang="en">
<head>
<meta charset="utf-8">
<title>Maple Barber Shop – Business Card</title>
<link rel="stylesheet" href="https://fonts.googleapis.com/css2?family=Cinzel:wght@700&family=Montserrat:wght@500&display=swap">
<style>
  :root {
    --stage: #e4e4e6;
    --navy-deep: #05081f;
    --navy: #0f1a5c;
    --navy-bright: #22358f;
    --paper: #fbfbfc;
    --ink-light: #eef0f8;
    --tool-grey: #d9dadd;
    --shadow: rgba(0, 0, 0, 0.22);
  }
  * { margin: 0; padding: 0; box-sizing: border-box; }
  html, body { width: 1200px; height: 799px; overflow: hidden; }
  body {
    background: var(--stage);
    display: flex;
    align-items: center;
    justify-content: center;
    gap: 60px;
  }
  .card {
    position: relative;
    width: 520px;
    height: 297px;
    border-radius: 18px;
    overflow: hidden;
    box-shadow: 0 14px 30px var(--shadow);
  }

  /* Back side */
  .card--back { background: var(--paper); }
  .tool {
    position: absolute;
    background: var(--tool-grey);
    opacity: 0.55;
    border-radius: 10px;
  }
  .tool--shears-top { left: 26px; top: 28px; width: 78px; height: 34px; }
  .tool--comb { left: 22px; top: 128px; width: 36px; height: 92px; }
  .tool--dryer { right: 30px; top: 100px; width: 62px; height: 92px; border-radius: 30px 30px 10px 10px; }
  .tool--shears-bottom { right: 34px; bottom: 20px; width: 52px; height: 58px; }
  .emblem {
    position: absolute;
    left: 50%; top: 50%;
    width: 250px; height: 172px;
    transform: translate(-50%, -50%);
    border-radius: 50%;
    background: radial-gradient(ellipse at 50% 40%, var(--navy-bright) 0%, var(--navy) 55%, var(--navy-deep) 100%);
    display: flex; align-items: center; justify-content: center;
  }

  .brand-name {
    font-family: "Cinzel", serif;
    font-weight: 700;
    color: var(--ink-light);
    text-align: center;
    line-height: 1.05;
  }
  .emblem .brand-name { font-size: 27px; letter-spacing: 1px; }

  /* Front side */
  .card--front {
    background: linear-gradient(160deg, var(--navy-deep) 0%, var(--navy) 55%, var(--navy-deep) 100%);
  }
  .card--front .sweep { position: absolute; inset: 0; }
  .card--front .brand-name {
    position: absolute;
    right: 60px; top: 46px;
    width: 250px;
    font-size: 32px;
    letter-spacing: 1.5px;
  }
  .contacts {
    position: absolute;
    left: 28px; right: 24px; bottom: 34px;
    display: grid;
    grid-template-columns: 1fr 1fr;
    row-gap: 18px;
    column-gap: 20px;
    font-family: "Montserrat", sans-serif;
    font-weight: 500;
    font-size: 11px;
    letter-spacing: 0.4px;
    color: var(--ink-light);
  }
  .contact { display: flex; align-items: center; gap: 8px; }
  .contact-icon {
    flex: none;
    width: 18px; height: 18px;
    border-radius: 50%;
    background: var(--ink-light);
    display: flex; align-items: center; justify-content: center;
  }
  .contact-icon svg { width: 10px; height: 10px; fill: var(--navy); }
</style>
</head>
<body>

<section class="card card--back" aria-label="Business card, back side">
  <div class="tool tool--shears-top" role="img" aria-label="Faint barber shears illustration"></div>
  <div class="tool tool--comb" role="img" aria-label="Faint comb illustration"></div>
  <div class="tool tool--dryer" role="img" aria-label="Faint hair dryer illustration"></div>
  <div class="tool tool--shears-bottom" role="img" aria-label="Faint scissors illustration"></div>
  <div class="emblem">
    <p class="brand-name">Maple<br>Barber Shop</p>
  </div>
</section>

<section class="card card--front" aria-label="Business card, front side">
  <svg class="sweep" viewBox="0 0 520 297" aria-hidden="true">
    <defs>
      <radialGradient id="sweepGlow" cx="65%" cy="20%" r="70%">
        <stop offset="0" stop-color="#2a3fa0" stop-opacity="0.85"/>
        <stop offset="1" stop-color="#0f1a5c" stop-opacity="0"/>
      </radialGradient>
    </defs>
    <path d="M110 0 H520 V175 C430 215 250 200 110 0 Z" fill="url(#sweepGlow)"/>
    <path d="M110 0 C250 200 430 215 520 175" fill="none" stroke="#3b52b8" stroke-opacity="0.5" stroke-width="1.5"/>
  </svg>

  <p class="brand-name">Maple<br>Barber Shop</p>

  <div class="contacts">
    <div class="contact">
      <span class="contact-icon"><svg viewBox="0 0 10 10"><path d="M2 0.8 L3.6 0.8 L4.2 3 L3 3.8 C3.6 5.1 4.9 6.4 6.2 7 L7 5.8 L9.2 6.4 L9.2 8 C9.2 8.7 8.6 9.2 8 9.2 C4.2 9 1 5.8 0.8 2 C0.8 1.4 1.3 0.8 2 0.8 Z"/></svg></span>
      <span>555 014 2290</span>
    </div>
    <div class="contact">
      <span class="contact-icon"><svg viewBox="0 0 10 10"><path d="M2 0.8 L3.6 0.8 L4.2 3 L3 3.8 C3.6 5.1 4.9 6.4 6.2 7 L7 5.8 L9.2 6.4 L9.2 8 C9.2 8.7 8.6 9.2 8 9.2 C4.2 9 1 5.8 0.8 2 C0.8 1.4 1.3 0.8 2 0.8 Z"/></svg></span>
      <span>555 014 7731</span>
    </div>
    <div class="contact">
      <span class="contact-icon"><svg viewBox="0 0 10 10"><path d="M5 0.5 C3 0.5 1.6 2 1.6 3.8 C1.6 6.3 5 9.5 5 9.5 C5 9.5 8.4 6.3 8.4 3.8 C8.4 2 7 0.5 5 0.5 Z M5 2.5 A1.3 1.3 0 1 1 5 5.1 A1.3 1.3 0 1 1 5 2.5 Z"/></svg></span>
      <span>418 ELM RD SUITE 1 BROOKVALE, NY 10000</span>
    </div>
    <div class="contact">
      <span class="contact-icon"><svg viewBox="0 0 10 10"><path d="M0.8 2 H9.2 V8 H0.8 Z M1.4 2.6 L5 5.4 L8.6 2.6" stroke="#0f1a5c" stroke-width="0.6" fill="#eef0f8"/></svg></span>
      <span>maplebarbershop@examplemail.com</span>
    </div>
  </div>
</section>

</body>
</html>
```